design a construction company business card

Design business card around our logo. Card must have all the typical info: name, title, address, phone, email, business name, etc. Somewhere on the card I would like to see our motto "Built on integrity... Inspired by commitment." Consider adding a splash of bright orange to the card to complement the blues and silvers/grays in the logo. We are open to metallic inks, textures, etc. We would like to see options on both light and dark backgrounds. The font in the logo is Euro Technic Extended Regular.

```html
<!DOCTYPE html>
<html lang="en">
<head>
<meta charset="utf-8">
<title>Halvorsen Contracting – Business Card</title>
<link rel="stylesheet" href="https://fonts.googleapis.com/css2?family=Arimo:ital,wght@0,400;0,700;1,700&display=swap">
<style>
  :root{
    --bg:#e4e5e7;
    --navy-deep:#1e2a3d;
    --navy:#27466e;
    --blue-glow:#3a73ad;
    --brand-blue:#2f5fae;
    --accent-orange:#f5a31a;
    --ink:#222326;
    --ink-soft:#55585e;
    --band-black:#1b1c1f;
    --white:#ffffff;
  }
  *{margin:0;padding:0;box-sizing:border-box}
  html,body{width:1200px;height:1200px;overflow:hidden;background:var(--bg);font-family:"Arimo",Arial,sans-serif}
  .canvas{position:relative;width:1200px;height:1200px}
  .card{position:absolute;left:250px;width:700px;height:400px;box-shadow:0 18px 40px rgba(0,0,0,.18)}

  /* front */
  .card-front{top:150px;background:radial-gradient(ellipse at 50% 55%,var(--blue-glow) 0%,var(--navy) 40%,var(--navy-deep) 100%);display:flex;align-items:center;justify-content:center}
  .front-brand{display:flex;flex-direction:column;align-items:center;color:var(--white);font-weight:700;letter-spacing:.08em}
  .front-brand .brand-name{font-size:62px;line-height:1}
  .front-brand .brand-sub{font-size:20px;margin-top:10px;letter-spacing:.18em}

  /* back */
  .card-back{top:650px;background:var(--white);overflow:hidden}
  .name-block{position:absolute;left:64px;top:40px;padding-left:22px}
  .name-block::before{content:"";position:absolute;left:0;top:2px;width:8px;height:40px;background:var(--accent-orange)}
  .person-name{font-size:30px;font-weight:400;color:var(--ink);letter-spacing:.02em}
  .person-title{font-size:14px;color:var(--ink-soft);margin-top:2px}
  .contact-list{position:absolute;left:40px;top:150px;list-style:none}
  .contact-list li{display:flex;align-items:center;gap:14px;height:34px;font-size:15px;color:var(--ink-soft)}
  .contact-list svg{width:24px;height:24px}
  .brand-mark{position:absolute;right:40px;top:150px;text-align:center;color:var(--brand-blue);font-weight:700;letter-spacing:.08em}
  .brand-mark .brand-name{font-size:46px;line-height:1}
  .brand-mark .brand-sub{font-size:14px;margin-top:6px;letter-spacing:.16em}
  .address{position:absolute;right:40px;top:250px;display:flex;gap:12px;align-items:flex-start;font-size:14px;color:var(--ink-soft);text-align:right;line-height:1.35}
  .address svg{width:24px;height:26px;order:2}
  .motto-band{position:absolute;left:0;right:0;bottom:0;height:70px;background:var(--band-black)}
  .motto-strip{position:absolute;left:0;right:60px;top:14px;height:42px;background:linear-gradient(90deg,var(--navy) 0%,var(--blue-glow) 45%,var(--navy) 100%);display:flex;align-items:center;justify-content:center;color:var(--white);font-weight:700;font-style:italic;font-size:22px;letter-spacing:.02em;white-space:nowrap}
</style>
</head>
<body>
<main class="canvas">
  <section class="card card-front">
    <div class="front-brand">
      <span class="brand-name">HALVORSEN</span>
      <span class="brand-sub">CONTRACTING, INC.</span>
    </div>
  </section>

  <section class="card card-back">
    <div class="name-block">
      <h1 class="person-name">DANIEL REYES</h1>
      <p class="person-title">General Contractor</p>
    </div>

    <ul class="contact-list">
      <li>
        <svg viewBox="0 0 24 24" aria-hidden="true"><circle cx="12" cy="12" r="10.5" fill="var(--brand-blue)" stroke="var(--accent-orange)" stroke-width="2"/><path d="M8.5 7.5l2 2-1 1.3a7 7 0 0 0 3.7 3.7l1.3-1 2 2-1.3 1.5c-3.8-.4-7.8-4.4-8.2-8.2z" fill="var(--white)"/></svg>
        <span>555-014-2387</span>
      </li>
      <li>
        <svg viewBox="0 0 24 24" aria-hidden="true"><circle cx="12" cy="12" r="10.5" fill="var(--brand-blue)" stroke="var(--accent-orange)" stroke-width="2"/><rect x="6.5" y="8" width="11" height="8" fill="none" stroke="var(--white)" stroke-width="1.4"/><path d="M6.5 8l5.5 4.5L17.5 8" fill="none" stroke="var(--white)" stroke-width="1.4"/></svg>
        <span>dreyes@halvorsenbuilds.com</span>
      </li>
      <li>
        <svg viewBox="0 0 24 24" aria-hidden="true"><circle cx="12" cy="12" r="10.5" fill="var(--brand-blue)" stroke="var(--accent-orange)" stroke-width="2"/><circle cx="12" cy="12" r="5.5" fill="none" stroke="var(--white)" stroke-width="1.3"/><path d="M6.5 12h11M12 6.5c-2.5 3-2.5 8 0 11M12 6.5c2.5 3 2.5 8 0 11" fill="none" stroke="var(--white)" stroke-width="1.1"/></svg>
        <span>www.halvorsenbuilds.com</span>
      </li>
    </ul>

    <div class="brand-mark">
      <div class="brand-name">HALVORSEN</div>
      <div class="brand-sub">CONTRACTING, INC.</div>
    </div>

    <div class="address">
      <svg viewBox="0 0 24 26" aria-hidden="true"><circle cx="12" cy="11" r="10" fill="none" stroke="var(--accent-orange)" stroke-width="2"/><path d="M12 5a4.5 4.5 0 0 1 4.5 4.5c0 3.5-4.5 8-4.5 8s-4.5-4.5-4.5-8A4.5 4.5 0 0 1 12 5z" fill="var(--brand-blue)"/><circle cx="12" cy="9.5" r="1.6" fill="var(--white)"/></svg>
      <span>4120 Larkspur Ave. Houston<br>TX 77008</span>
    </div>

    <div class="motto-band">
      <p class="motto-strip">“Rooted in honesty…Driven by dedication”</p>
    </div>
  </section>
</main>
</body>
</html>
```